New Business Card for chocolate Company

I am looking to have business cards for my Chocolate Company Velvet Hollow Sweets.
I hand make all organic, fair trade, vegan, gluten free, allergy friendly chocolate. We are located in Austin Texas and are very Proud to be a locally made good. I have my logo and new sticker design for our boxes but now I need cards. I was thinking either natural craft or white. But I want to have a bit of funk to the cards so someone will hold onto it for a long time.
The important info is
Dana Pelworth
Owner and Chocolatier
Velvet Hollow Sweets
velvethollowsweetsatx.com
velvethollowsweets@brivomail.com
velvethollowsweets on instagram
512.373.4816

Velvet Hollow sweets are Vegan ,Gluten free, organic, fair trade, allergy friendly hand made chocolate.

Target Market(s)

We cater to all ages. Our chocolate is on the higher price scale and is a decadent treat. But we make custom molds for any event kids party's to an elegant wedding.

Industry/Entity Type

Business

Requirements
Must have
• Good design logo and some sort of austin vibe.

```html
<!DOCTYPE html>
<html lang="en">
<head>
<meta charset="utf-8">
<title>Velvet Hollow Sweets – Business Card</title>
<link rel="stylesheet" href="https://fonts.googleapis.com/css2?family=Oswald:wght@300;400&family=Roboto+Condensed:wght@400;700&family=Questrial&display=swap">
<style>
  :root {
    --canvas: #ffffff;
    --card: #ffffff;
    --card-edge: #9a9a9a;
    --red: #d31f3a;
    --band-light: #d4e0e4;
    --band-dark: #b1c7cd;
    --label: #111111;
  }
  * { margin: 0; padding: 0; box-sizing: border-box; }
  html, body { width: 1200px; height: 1000px; overflow: hidden; background: var(--canvas); }
  .stage { position: relative; width: 1200px; height: 1000px; }

  .card {
    position: absolute; left: 240px; width: 717px; height: 407px;
    background: var(--card); border: 1px solid var(--card-edge);
    box-shadow: 6px 12px 18px rgba(0,0,0,0.14);
    overflow: hidden; color: var(--red);
  }
  .card--front { top: 45px; }
  .card--back { top: 539px; }

  .card__bands { position: absolute; inset: 0; width: 100%; height: 100%; }

  .side-label {
    position: absolute; left: 1003px; font-family: "Questrial", sans-serif;
    font-size: 42px; color: var(--label);
  }
  .side-label--front { top: 398px; }
  .side-label--back { top: 890px; }

  .brand {
    position: absolute; left: 268px; top: 92px; width: 180px; height: 180px;
    border-radius: 50%; background: var(--card);
    display: flex; flex-direction: column; align-items: center; justify-content: center;
    font-family: "Oswald", sans-serif; font-weight: 400; color: var(--red);
    font-size: 30px; line-height: 1.05; text-transform: uppercase; text-align: center;
  }

  .centered { position: absolute; transform: translateX(-50%); text-align: center; white-space: nowrap; }

  .owner__name { left: 135px; top: 150px; font-family: "Oswald", sans-serif; font-weight: 300; font-size: 29px; }
  .owner__title { left: 135px; top: 189px; font-family: "Roboto Condensed", sans-serif; font-size: 12px; text-transform: uppercase; }

  .qualities { left: 583px; top: 106px; font-family: "Oswald", sans-serif; font-weight: 300; font-size: 15px; line-height: 20px; font-variant: small-caps; }
  .star { font-size: 14px; line-height: 14px; }

  .contact { left: 358px; top: 323px; font-family: "Roboto Condensed", sans-serif; font-size: 15px; line-height: 22px; }
  .contact__phone { font-weight: 700; font-size: 16px; letter-spacing: 0.5px; }
  .brace { position: absolute; top: 315px; font-family: "Oswald", sans-serif; font-weight: 300; font-size: 68px; line-height: 1; }
  .brace--open { left: 232px; }
  .brace--close { left: 468px; }

  .tagline { top: 164px; font-family: "Oswald", sans-serif; font-weight: 300; font-size: 26px; }
  .tagline--left { left: 160px; }
  .tagline--right { left: 560px; }
  .back-star { left: 358px; color: #ffffff; font-size: 22px; }
  .back-star--top { top: 56px; }
  .back-star--bottom { top: 292px; }
  .website { left: 358px; top: 336px; font-family: "Oswald", sans-serif; font-weight: 400; font-size: 23px; letter-spacing: 0.3px; }
</style>
</head>
<body>
<main class="stage">

  <section class="card card--front" aria-label="Card front">
    <svg class="card__bands" viewBox="0 0 717 407" aria-hidden="true">
      <polygon fill="var(--band-light)" points="295,0 415,0 385,407 325,407"/>
      <polygon fill="var(--band-dark)" points="327,0 387,0 372,204 392,407 318,407 340,204"/>
    </svg>

    <div class="brand">Velvet<br>Hollow<br>Sweets</div>

    <div class="centered owner__name">DANA PELWORTH</div>
    <div class="centered owner__title">★ Owner and Chocolatier ★</div>

    <div class="centered qualities">
      <div class="star">★</div>
      <div>Vegan</div>
      <div>Gluten free</div>
      <div>Fair trade chocolate</div>
      <div>Allergy friendly</div>
      <div>Organic</div>
      <div class="star">★</div>
    </div>

    <span class="brace brace--open">{</span>
    <div class="centered contact">
      <div>velvethollowsweets@brivomail.com</div>
      <div>Instagram :velvethollowsweets</div>
      <div class="contact__phone">512.373.4816</div>
    </div>
    <span class="brace brace--close">}</span>
  </section>
  <div class="side-label side-label--front">front</div>

  <section class="card card--back" aria-label="Card back">
    <svg class="card__bands" viewBox="0 0 717 407" aria-hidden="true">
      <polygon fill="var(--band-light)" points="302,0 415,0 417,407 300,407"/>
      <polygon fill="var(--band-dark)" points="335,0 378,0 372,204 382,407 335,407 344,204"/>
    </svg>

    <div class="centered back-star back-star--top">★</div>
    <div class="brand">Velvet<br>Hollow<br>Sweets</div>
    <div class="centered back-star back-star--bottom">★</div>

    <div class="centered tagline tagline--left">LOCALLY MADE</div>
    <div class="centered tagline tagline--right">IN AUSTIN TEXAS</div>

    <div class="centered website">WWW.VELVETHOLLOWSWEETSATX.COM</div>
  </section>
  <div class="side-label side-label--back">back</div>

</main>
</body>
</html>
```